Quillory homepage (design only)

We need a high-impact design (alone) for the homepage for a new service to be launched shortly.

Quillory.com will allow consumers to generate a free 'financial personality' report which will help people protect themselves from being mis-sold inappropriate products and services by the financial services industry.

We have upload the Quillory logo and associated artwork. You have totally free reign to use these as you see fit, including using different colours to the lime green we've used.

We ONLY want a design and would prefer it in Illustrator CS5 or lower format rather than Photoshop bitmap. We will write any necessary code or CSS for the final page.

We intend the end site to utilise html5 type animation and effects extensively so if you are picturing an animation, please ensure you explain it with your submission.

The homepage will have five main elements:

1. Navigation:
- Why Quillory
- Security
- Sample report
- Do the test

2. Main section - Quillory : Know Your Financial Personality (you can add ipsum lorum 'explanatory text' if you see fit). This section should refer to the services output, a report which shows five financial characteristics:
- Personality type
- Investment approach
- Knowledge
- Decision biases
- % of UK population like you

3. 'See how you compare against the UK'. An important output of the report is the fact it is linked to extensive UK research. When a user has completed the test, Quillory show him or her via an info graphic, whist percentage of the UK population shares their attributes. Accompnaying tex reads: " If you've ever wondered how you compare to others when it comes to your attitudes on money related matters, quillory will show you". There is an attached file called 'infographic' that illustrates what the end infogrpahic might look like. You can choose to refer to this or elements of this in this section if you choose.

4. 'Cut out the stuff not relevant to you' Accompanying text could be: "Whether it’s language, unnecessarily complex products or stuff that may be too plain risky for you, your Quillory report will help filter out all of the stuff that’s less relevant to you leaving you with choices you understand and decisions that are easier to make." we imagine this section leading to a page that will explain the complexity of products and services before a Quillory report and the small number of relevant services after a quillory report. This section should illustrate that before and after concept.

5. 'Take the test' This section is critical, its the 'call to action' element of the page that links straight to the test. It should illustrate that the test is very short, and very easy.. only two very interactive steps before you get results:
1. Click on the graphics that best describe you.
2. Drag some questions into Quillory 'answer buckets'
3. Done! See the results.
4. Give your free profile to any online service (we make it simple)

The emphasis here is on illustration, typography, colour and impact. We want the site to feel consumer and accessible, not too stuffy and financial, at the same time not too childlike. We are not in favour of typical 'financial' library pics, we'd prefer illustration. Please use your own creativity

Target Market(s)

Adults typically aged 30+ with majority in 40's - 60's. People considering investing or taking any kind of financial advice,

Industry/Entity Type

Financial

Font styles to use
Sans Serif

Requirements
Must have
• The design must include the attached quillory logo albeit the colours used can be entirely at your discretion.
Nice to have
• Site designs we like include:
http://www.fennelvault.example

Should not have
• Design should not contain 'bamboo' clip art. If any quillory type artwork is needed, if should be a derivative of the attached 'bamboo stalk' file. Ideally no stock photography. Illustration and typography should dominate.

Should not use serif fonts

```html
<!DOCTYPE html>
<html lang="en">
<head>
<meta charset="utf-8">
<title>Quillory — Know Your Financial Personality</title>
<link rel="stylesheet" href="https://fonts.googleapis.com/css2?family=Roboto+Condensed:wght@400;700&family=Open+Sans:ital,wght@0,400;0,600;0,700;1,400&display=swap">
<style>
:root{
  --navy:#2e3b4c;
  --navy-dark:#27323f;
  --green:#7cc142;
  --green-dark:#3d5a1f;
  --green-mid:#5e8f32;
  --orange:#f26a36;
  --ink:#222;
  --muted:#555;
  --white:#fff;
  --pale:#dcefc9;
}
*{box-sizing:border-box;margin:0;padding:0}
html,body{width:1200px;height:3237px;overflow:hidden}
body{position:relative;font-family:"Open Sans",Arial,sans-serif;color:var(--ink);background:var(--white)}
.abs{position:absolute}
.heading{font-family:"Roboto Condensed","Arial Narrow",sans-serif;font-weight:700;text-transform:uppercase;letter-spacing:.2px}

/* top bar */
.topbar{position:absolute;left:0;top:0;width:1200px;height:32px;background:var(--navy)}
.topbar__call{position:absolute;left:100px;top:8px;font-size:12px;color:var(--white)}
.topbar__social{position:absolute;top:7px;width:18px;height:18px;border-radius:50%;background:#fff;opacity:.9}

/* nav */
.nav{position:absolute;left:0;top:32px;width:1200px;height:83px;background:var(--white);border-bottom:1px solid #e4e4e4}
.brand{position:absolute;left:88px;top:20px;display:flex;align-items:center;gap:10px}
.brand__dot{width:44px;height:44px;border-radius:50%;background:var(--green)}
.brand__name{font-family:"Open Sans",sans-serif;font-weight:600;font-size:30px;color:var(--ink)}
.nav__item{position:absolute;top:0;height:83px;line-height:83px;font-family:"Roboto Condensed",sans-serif;font-size:14px;text-transform:uppercase;color:var(--ink)}
.nav__item--active{background:var(--green);color:var(--white);padding:0 14px}
.nav__search{position:absolute;left:1078px;top:22px;width:38px;height:38px}

/* hero */
.hero{position:absolute;left:0;top:115px;width:1200px;height:479px;background:var(--navy)}
.hero__art{position:absolute;left:86px;top:100px;width:440px;height:292px;border-radius:8px;background:linear-gradient(135deg,#5d6b7c,#3c4a5b)}
.hero__title{position:absolute;left:572px;top:137px;font-size:40px;color:var(--green)}
.hero__lead{position:absolute;left:575px;top:190px;font-size:19px;color:var(--white)}
.hero__btn{position:absolute;left:578px;top:308px;width:220px;height:56px;background:var(--green);color:var(--white);font-family:"Roboto Condensed",sans-serif;font-weight:700;font-size:22px;line-height:56px;text-align:center}

/* section shared */
.section-title{position:absolute;left:0;width:1200px;text-align:center;font-size:40px}
.section-sub{position:absolute;left:0;width:1200px;text-align:center;font-size:19px;color:var(--green)}

/* features tree */
.tree{position:absolute;left:0;top:594px;width:1200px;height:820px}
.tree__svg{position:absolute;left:0;top:0}
.feature{position:absolute;width:200px}
.feature__title{font-size:20px;color:var(--ink);line-height:1.2}
.feature__body{font-size:11.5px;color:var(--muted);line-height:1.45;margin-top:4px}

/* compare */
.compare{position:absolute;left:0;top:1414px;width:1200px;height:776px;background:var(--green)}
.compare .section-title{color:var(--navy)}
.compare .section-sub{color:var(--white)}
.compare__text{position:absolute;left:156px;top:150px;width:890px;font-size:17px;line-height:1.45;color:var(--white)}
.compare__graph{position:absolute;left:0;top:0}
.compare__graph text{font-family:"Open Sans",sans-serif}

/* filter list */
.filters{position:absolute;left:0;top:2190px;width:1200px;height:587px}
.filter{position:absolute;left:216px;width:800px}
.filter__icon{position:absolute;left:0;top:0;width:90px;height:80px}
.filter__title{position:absolute;left:97px;top:-4px;font-family:"Roboto Condensed",sans-serif;font-weight:700;font-size:22px;text-transform:uppercase}
.filter__body{position:absolute;left:97px;top:34px;width:700px;font-size:12px;line-height:1.8;color:var(--ink)}

/* testimonial */
.testimonial{position:absolute;left:0;top:2777px;width:1200px;height:363px;background:var(--navy)}
.testimonial .section-title{color:var(--white)}
.testimonial__avatar{position:absolute;left:575px;top:128px;width:88px;height:88px;border-radius:50%;border:4px solid var(--green);background:linear-gradient(160deg,#c9d1d8,#8f9aa5)}
.testimonial__quote{position:absolute;left:282px;top:238px;width:670px;font-size:12px;font-style:italic;line-height:1.6;color:var(--white)}
.testimonial__mark{position:absolute;font-family:"Open Sans",sans-serif;font-weight:700;font-size:60px;color:var(--green);line-height:1}
.testimonial__name{position:absolute;left:0;top:300px;width:1200px;text-align:center;font-size:13px;font-weight:700;font-style:italic;color:var(--green)}

/* footer */
.footer{position:absolute;left:0;top:3140px;width:1200px;height:97px;background:var(--white)}
.footer__nav{position:absolute;left:0;top:32px;width:1200px;display:flex;justify-content:center;gap:44px}
.footer__item{font-family:"Roboto Condensed",sans-serif;font-size:14px;text-transform:uppercase;padding-bottom:6px}
.footer__item--active{border-bottom:3px solid var(--green)}
</style>
</head>
<body>

<header class="topbar">
  <span class="topbar__call">Call Us Now :555-014-2277</span>
  <span class="topbar__social" style="left:964px"></span>
  <span class="topbar__social" style="left:1003px"></span>
  <span class="topbar__social" style="left:1042px"></span>
  <span class="topbar__social" style="left:1081px"></span>
</header>

<nav class="nav">
  <div class="brand"><span class="brand__dot"></span><span class="brand__name">Quillory</span></div>
  <span class="nav__item nav__item--active" style="left:565px">Why Quillory</span>
  <span class="nav__item" style="left:702px">Security</span>
  <span class="nav__item" style="left:797px">Sample Report</span>
  <span class="nav__item" style="left:930px">Do the Test</span>
  <svg class="nav__search" viewBox="0 0 38 38"><circle cx="19" cy="19" r="17" fill="none" stroke="#222" stroke-width="2"/><circle cx="17" cy="17" r="6" fill="none" stroke="#222" stroke-width="2.2"/><line x1="21.5" y1="21.5" x2="26" y2="26" stroke="#222" stroke-width="2.4" stroke-linecap="round"/></svg>
</nav>

<section class="hero">
  <div class="hero__art" role="img" aria-label="Illustration of a desktop monitor and tablet showing the Quillory name, with a cartoon guide presenting them"></div>
  <h1 class="hero__title heading">Lorem ipsum dolor sit amet</h1>
  <p class="hero__lead">Lorem ipsum dolor sit amet, consectetur adipisicing elit</p>
  <a class="hero__btn">LOREM IPSUM</a>
</section>

<section class="tree">
  <h2 class="section-title heading" style="top:42px">Lorem ipsum dolor sit amet</h2>
  <p class="section-sub" style="top:94px">Lorem ipsum dolor sit amet, consectetur adipisicing elit</p>
  <svg class="tree__svg" width="1200" height="820" viewBox="0 0 1200 820">
    <g stroke="#7cc142" stroke-width="2" fill="none">
      <line x1="535" y1="205" x2="535" y2="647"/>
      <line x1="300" y1="321" x2="535" y2="321"/>
      <line x1="300" y1="530" x2="535" y2="530"/>
      <line x1="535" y1="205" x2="750" y2="205"/>
      <line x1="535" y1="425" x2="750" y2="425"/>
      <line x1="535" y1="647" x2="750" y2="647"/>
    </g>
    <g fill="#7cc142">
      <circle cx="282" cy="321" r="26"/><circle cx="282" cy="530" r="26"/>
      <circle cx="773" cy="209" r="26"/><circle cx="773" cy="425" r="26"/><circle cx="773" cy="645" r="26"/>
    </g>
    <g stroke="#fff" stroke-width="2.4" fill="none" stroke-linecap="round" stroke-linejoin="round">
      <path d="M270 326a8 8 0 0 1 4-15 10 10 0 0 1 18 2 7 7 0 0 1 2 13"/><path d="M282 331v-12M277 323l5-5 5 5"/>
      <rect x="268" y="519" width="28" height="18" rx="1"/><path d="M277 543h10M282 537v6"/>
      <path d="M762 203h22v12h-14l-6 5v-5h-2z"/>
      <rect x="760" y="416" width="26" height="18" rx="2"/><path d="M760 422h26M765 429h6"/>
      <circle cx="773" cy="645" r="5"/><path d="M773 633v5M773 652v5M761 645h5M780 645h5M765 637l3 3M778 650l3 3M781 637l-3 3M768 650l-3 3"/>
    </g>
  </svg>
  <div class="feature" style="left:320px;top:335px"><div class="feature__title">Lorem ipsum dolor</div><div class="feature__body">Lorem ipsum dolor sit amet, consectetur adipisicing elit, sed do eiusmod tempor incididunt</div></div>
  <div class="feature" style="left:320px;top:544px"><div class="feature__title">Lorem ipsum dolor</div><div class="feature__body">Lorem ipsum dolor sit amet, consectetur adipisicing elit, sed do eiusmod tempor incididunt</div></div>
  <div class="feature" style="left:552px;top:218px"><div class="feature__title">Lorem ipsum dolor</div><div class="feature__body">Lorem ipsum dolor sit amet, consectetur adipisicing elit, sed do eiusmod tempor incididunt</div></div>
  <div class="feature" style="left:552px;top:438px"><div class="feature__title">Lorem ipsum dolor</div><div class="feature__body">Lorem ipsum dolor sit amet, consectetur adipisicing elit, sed do eiusmod tempor incididunt</div></div>
  <div class="feature" style="left:552px;top:656px"><div class="feature__title">Lorem ipsum dolor</div><div class="feature__body">Lorem ipsum dolor sit amet, consectetur adipisicing elit, sed do eiusmod tempor incididunt</div></div>
</section>

<section class="compare">
  <h2 class="section-title heading" style="top:42px">Lorem ipsum dolor sit amet</h2>
  <p class="section-sub" style="top:92px">Lorem ipsum dolor sit amet, consectetur adipisicing elit</p>
  <p class="compare__text">Lorem ipsum dolor sit amet, consectetur adipisicing elit, sed do eiusmod tempor incididunt ut labore et dolore magna aliqua. Ut enim ad minim veniam, quis nostrud exercitation ullamco laboris nisi ut aliquip ex ea commodo consequat. Duis aute irure dolor in reprehenderit in voluptate velit esse cillum dolore eu fugiat nulla pariatur. Excepteur sint occaecat cupidatat non proident, sunt in culpa qui officia deserunt mollit anim id est laborum.</p>
  <svg class="compare__graph" width="1200" height="776" viewBox="0 0 1200 776">
    <path d="M168 360V500Q168 524 192 524H435Q460 524 460 549V665Q460 690 485 690H955Q980 690 980 665V612" fill="none" stroke="#3d5a1f" stroke-width="9"/>
    <circle cx="168" cy="330" r="30" fill="none" stroke="#3d5a1f" stroke-width="9"/>
    <circle cx="980" cy="582" r="30" fill="#5e8f32" stroke="#3d5a1f" stroke-width="9"/>
    <text x="980" y="588" font-size="15" fill="#fff" text-anchor="middle" font-weight="700">11%</text>
    <text x="205" y="330" font-size="13" fill="#dcefc9">Alike</text>

    <g fill="#fff" stroke="#3d5a1f" stroke-width="3">
      <circle cx="205" cy="524" r="6"/><circle cx="283" cy="524" r="6"/>
      <circle cx="544" cy="690" r="6"/><circle cx="725" cy="690" r="6"/>
    </g>
    <g font-size="13" fill="#dcefc9" text-anchor="middle">
      <text x="205" y="552">Gender</text><text x="283" y="552">Age</text>
      <text x="564" y="717">Financial Knowledge</text><text x="750" y="717">Risk Aptitude</text>
    </g>

    <circle cx="201" cy="442" r="15" fill="#f26a36" stroke="#fff" stroke-width="2"/>
    <text x="201" y="446" font-size="10" fill="#fff" text-anchor="middle">61%</text>
    <text x="240" y="446" font-size="10" fill="#dcefc9" text-anchor="middle">39%</text>
    <rect x="197" y="465" width="10" height="22" fill="#4aa3d8"/><rect x="232" y="465" width="10" height="22" fill="#c58fb8"/>

    <g fill="#3d5a1f">
      <rect x="272" y="402" width="20" height="14"/><rect x="272" y="424" width="20" height="14"/>
      <rect x="272" y="446" width="20" height="14"/><rect x="272" y="468" width="20" height="14"/>
    </g>
    <g font-size="10" fill="#dcefc9">
      <text x="298" y="413">30% - 34%</text><text x="298" y="435" fill="#fff" font-weight="700">40%</text>
      <text x="298" y="457">50% - 28%</text><text x="298" y="479">60% - 15%</text>
    </g>
    <circle cx="339" cy="438" r="15" fill="#f26a36" stroke="#fff" stroke-width="2"/>
    <text x="339" y="442" font-size="10" fill="#fff" text-anchor="middle">32%</text>

    <g fill="#5e8f32" stroke="#7cc142" stroke-width="2">
      <circle cx="544" cy="431" r="24"/><circle cx="544" cy="565" r="26"/><circle cx="544" cy="643" r="26"/>
      <circle cx="742" cy="377" r="24"/><circle cx="742" cy="507" r="26"/><circle cx="742" cy="582" r="26"/><circle cx="742" cy="653" r="24"/>
    </g>
    <circle cx="544" cy="496" r="30" fill="#f26a36" stroke="#fff" stroke-width="5"/>
    <circle cx="742" cy="435" r="20" fill="#f26a36" stroke="#fff" stroke-width="4"/>
    <g font-size="12" fill="#dcefc9" text-anchor="middle">
      <text x="544" y="435">17%</text><text x="544" y="500" fill="#fff" font-weight="700" font-size="14">28%</text>
      <text x="544" y="569" fill="#fff" font-weight="700">27%</text><text x="544" y="647">28%</text>
      <text x="742" y="381">19%</text><text x="742" y="439" fill="#fff" font-weight="700">16%</text>
      <text x="742" y="511">23%</text><text x="742" y="586">23%</text><text x="742" y="657">19%</text>
    </g>
    <g font-size="10" fill="#dcefc9">
      <text x="583" y="434">Financially savvy</text>
      <text x="583" y="499" fill="#fff" font-weight="700">Competent</text>
      <text x="583" y="568">Some knowledge</text>
      <text x="583" y="646">Basic knowledge</text>
      <text x="781" y="380">Risk averse</text>
      <text x="781" y="438" fill="#fff" font-weight="700">Platform builder</text>
      <text x="781" y="502">Risk tolerant</text><text x="781" y="515">&amp; product focused</text>
      <text x="781" y="577">Risk averse</text><text x="781" y="590">&amp; advice focused</text>
      <text x="781" y="648">Risk averse</text><text x="781" y="661">&amp; advice focused</text>
      <text x="945" y="462" fill="#4aa3d8">% like me</text>
    </g>
    <g fill="#4aa3d8">
      <rect x="952" y="472" width="8" height="10"/><rect x="963" y="472" width="8" height="10"/><rect x="974" y="472" width="8" height="10"/><rect x="985" y="472" width="8" height="10"/><rect x="996" y="472" width="8" height="10"/>
    </g>
    <g fill="#3d5a1f">
      <rect x="952" y="486" width="8" height="10"/><rect x="963" y="486" width="8" height="10"/><rect x="974" y="486" width="8" height="10"/><rect x="985" y="486" width="8" height="10"/><rect x="996" y="486" width="8" height="10"/>
      <rect x="952" y="500" width="8" height="10"/><rect x="963" y="500" width="8" height="10"/><rect x="974" y="500" width="8" height="10"/><rect x="985" y="500" width="8" height="10"/><rect x="996" y="500" width="8" height="10"/>
    </g>
  </svg>
</section>

<section class="filters">
  <h2 class="section-title heading" style="top:40px">Lorem ipsum dolor sit amet</h2>
  <p class="section-sub" style="top:92px">Lorem ipsum dolor sit amet, consectetur adipisicing elit</p>

  <div class="filter" style="top:150px">
    <svg class="filter__icon" viewBox="0 0 90 80" fill="none" stroke="#7cc142" stroke-width="2.2" stroke-linejoin="round">
      <rect x="33" y="4" width="24" height="20" rx="4"/><rect x="8" y="30" width="24" height="20" rx="4"/><rect x="58" y="30" width="24" height="20" rx="4"/>
      <rect x="21" y="56" width="24" height="20" rx="4"/><rect x="47" y="56" width="24" height="20" rx="4"/><rect x="33" y="30" width="24" height="20" rx="4"/>
    </svg>
    <div class="filter__title">Lorem ipsum dolor</div>
    <p class="filter__body">Lorem ipsum dolor sit amet, consectetur adipisicing elit, sed do eiusmod tempor incididunt ut labore et dolore magna aliqua. Ut enim ad minim veniam, quis nostrud exercitation ullamco laboris nisi ut aliquip ex ea commodo consequat.</p>
  </div>

  <div class="filter" style="top:290px">
    <svg class="filter__icon" viewBox="0 0 90 80" fill="none" stroke="#7cc142" stroke-width="2.2" stroke-linecap="round">
      <path d="M35 52c0-8-9-12-9-24a19 19 0 0 1 38 0c0 12-9 16-9 24z"/><path d="M37 58h16M38 64h14M41 70h8"/>
      <path d="M45 2v5M18 14l4 3M72 14l-4 3M12 30h5M73 30h5"/>
    </svg>
    <div class="filter__title">Lorem ipsum dolor</div>
    <p class="filter__body">Lorem ipsum dolor sit amet, consectetur adipisicing elit, sed do eiusmod tempor incididunt ut labore et dolore magna aliqua. Ut enim ad minim veniam, quis nostrud exercitation ullamco laboris nisi ut aliquip ex ea commodo consequat.</p>
  </div>

  <div class="filter" style="top:428px">
    <svg class="filter__icon" viewBox="0 0 90 80" fill="none" stroke="#7cc142" stroke-width="2.2" stroke-linejoin="round" stroke-linecap="round">
      <path d="M20 40h50"/><path d="M26 40v34h38V40"/><path d="M26 50h38"/>
      <path d="M45 10v8M41 14h8M28 20l3 3M62 20l-3 3M35 30h0M56 28h0"/>
    </svg>
    <div class="filter__title">Lorem ipsum dolor</div>
    <p class="filter__body">Lorem ipsum dolor sit amet, consectetur adipisicing elit, sed do eiusmod tempor incididunt ut labore et dolore magna aliqua. Ut enim ad minim veniam, quis nostrud exercitation ullamco laboris nisi ut aliquip ex ea commodo consequat.</p>
  </div>
</section>

<section class="testimonial">
  <h2 class="section-title heading" style="top:42px">Lorem ipsum dolor sit amet</h2>
  <div class="testimonial__avatar" role="img" aria-label="Round portrait photo of the customer giving the testimonial"></div>
  <span class="testimonial__mark" style="left:250px;top:228px">“</span>
  <p class="testimonial__quote">Lorem ipsum dolor sit amet, consectetur adipisicing elit, sed do eiusmod tempor incididunt ut labore et dolore magna aliqua. Ut enim ad minim veniam, quis nostrud exercitation ullamco laboris nisi ut aliquip ex ea commodo consequat.</p>
  <span class="testimonial__mark" style="left:958px;top:268px">”</span>
  <p class="testimonial__name">Orrin.</p>
</section>

<footer class="footer">
  <div class="footer__nav">
    <span class="footer__item footer__item--active">Why Quillory</span>
    <span class="footer__item">Security</span>
    <span class="footer__item">Sample Report</span>
    <span class="footer__item">Do the Test</span>
  </div>
</footer>

</body>
</html>
```